Flyer-Design für Yoga-Studio
Zielgruppe
Yoga-Studio, Zielgruppe: alle Erwachsenen
Aufgabenstellung
Der Flyer soll nicht feminin wirken, eher in Grau-Blau oder Braun Tönen. Nicht überladen oder verschnörkelt. Es darf gerne ein Symbol darin vorkommen. Gerne DinA6 (Hinter und Forderseite)
Der Flyer ist für die Neueröffnung eines Yogastudios, alle wichtigen Infos sollen enthalten sein.

```html
<!DOCTYPE html>
<html lang="de">
<head>
<meta charset="utf-8">
<title>Morgen Yoga – Flyer</title>
<link href="https://fonts.googleapis.com/css2?family=Cinzel+Decorative:wght@400&family=Cinzel:wght@400&family=Montserrat:wght@300;400;700&display=swap" rel="stylesheet">
<style>
  :root {
    --page-bg: #e2e2e2;
    --sand-top: #e9b565;
    --sand-bottom: #d89e4e;
    --indigo: #233f80;
    --cream: #fbf6ee;
  }
  * { margin: 0; padding: 0; box-sizing: border-box; }
  html, body {
    width: 1200px; height: 1200px; overflow: hidden;
    background: var(--page-bg);
  }
  .flyer {
    position: absolute; left: 228px; top: 76px;
    width: 744px; height: 1048px; overflow: hidden;
    background: linear-gradient(180deg, var(--sand-top) 0%, var(--sand-bottom) 100%);
  }
  .ornament-field {
    position: absolute; left: 0; top: 240px; width: 744px; height: 808px;
    background: radial-gradient(ellipse at 50% 45%, rgba(190,140,70,0.28) 0%, rgba(190,140,70,0.08) 55%, rgba(190,140,70,0) 75%);
  }
  .figure-area {
    position: absolute; right: 0; top: 0; width: 68px; height: 1048px;
    background: var(--indigo);
  }
  .line { position: absolute; white-space: nowrap; line-height: 1; }
  .title {
    left: 33px; top: 64px;
    font-family: "Cinzel Decorative", serif; font-weight: 400; font-size: 62px; color: var(--indigo);
    letter-spacing: -1px;
  }
  .tagline {
    left: 33px; font-family: "Cinzel", serif; font-size: 28px; color: var(--cream);
    letter-spacing: -1px;
  }
  .tagline.one { top: 134px; }
  .tagline.two { top: 173px; }
  .tagline.three { top: 211px; }
  .days {
    left: 33px; font-family: "Cinzel", serif; font-size: 80px; color: var(--indigo);
    letter-spacing: -2px;
  }
  .days.one { top: 442px; }
  .days.two { top: 516px; }
  .address {
    left: 33px; top: 594px;
    font-family: "Montserrat", sans-serif; font-weight: 300; font-size: 27px; color: var(--cream);
    letter-spacing: -1px;
  }
  .time {
    left: 33px; top: 627px;
    font-family: "Montserrat", sans-serif; font-weight: 400; font-size: 34px; color: var(--indigo);
    letter-spacing: -1.5px;
  }
  .contact { position: absolute; left: 0; width: 744px; text-align: center; line-height: 1; }
  .question {
    top: 826px; font-family: "Cinzel", serif; font-size: 40px; color: var(--indigo);
    letter-spacing: -1px;
  }
  .signup {
    top: 866px; font-family: "Montserrat", sans-serif; font-weight: 400; font-size: 20px;
    color: var(--cream); letter-spacing: -0.8px;
  }
  .chat {
    top: 897px; font-family: "Montserrat", sans-serif; font-weight: 700; font-size: 30px;
    color: var(--cream); letter-spacing: -1.5px;
  }
  .follow {
    top: 948px; font-family: "Cinzel", serif; font-size: 17px; color: var(--indigo);
    letter-spacing: 5px;
  }
  .networks {
    top: 979px; font-family: "Montserrat", sans-serif; font-weight: 700; font-size: 15px;
    color: var(--cream); letter-spacing: 1px;
  }
  .networks span { margin: 0 10px; }
  .studio {
    top: 1008px; font-family: "Montserrat", sans-serif; font-weight: 400; font-size: 14px;
    color: var(--cream); letter-spacing: 3px;
  }
</style>
</head>
<body>
  <main class="flyer">
    <div class="ornament-field" role="img" aria-label="Dezentes Mandala-Ornament im Hintergrund"></div>
    <div class="figure-area" role="img" aria-label="Blaue Silhouette einer Person in Baum-Yogahaltung"></div>

    <h1 class="line title">Morgen Yoga</h1>
    <p class="line tagline one">AUSGEGLICHEN IN DEN TAG STARTEN</p>
    <p class="line tagline two">ENERGIEGELADEN</p>
    <p class="line tagline three">WACH</p>

    <p class="line days one">MONTAG</p>
    <p class="line days two">BIS FREITAG</p>
    <p class="line address">LINDENWEG 14 &nbsp;|&nbsp; 8400 TALBRUNN</p>
    <p class="line time">6.45 - 7.45 UHR</p>

    <p class="contact question">INTERESSIERT?</p>
    <p class="contact signup">ANMELDUNGEN (AUCH PROBELEKTIONEN) ODER FRAGEN</p>
    <p class="contact chat">CHAT AN LUKAS 07 9 444 55 66</p>
    <p class="contact follow">FOLLOW US ON</p>
    <p class="contact networks"><span>PINORA</span><span>FLIKTO</span></p>
    <p class="contact studio">RAVI YOGA</p>
  </main>
</body>
</html>
```